Screen Tides - Report on digital habits and attitudes

We are a research company and we have written a PowerPoint Report to present the results of a series of surveys conducted in the last three years. The research is about the "Screen Tides": people are facing the opportunities and challanges of their lives transformed by the digital technologies. We have investigated a number of topics through thousands of interviews and we've analyzed the data presented in the PowerPoint document.
We're not quite satisfied with the look and feel of the report: it looks too flat and boring, too "basic" to be presented as a professional work, yet being just that. We'd like you to upgrade the graphics and style of the report up to the level of a professional research product. The document still needs to be fully editable (either text and charts) but you can rearrange all the contents as you please, adding images, changing font and text size, colors and whatever you think is necessary to reach our goal.

Target Market(s)

Media covering digital issues
Marketing executives
Public institutions and policy makers

Industry/Entity Type

Market Research

Requirements
Must have
• The treats of a professional work
Fully editable within PowerPoint (either text and charts)
Nice to have
• Smart images
Original organization of the pages
Colors and graphics coherent with the corvalmeadow.it logo/website look and feel
Should not have
• PPT document over 30 MBytes
Images violating copyright

```html
<!DOCTYPE html>
<html lang="it">
<head>
<meta charset="utf-8">
<title>Screen Tides – Report design</title>
<link href="https://fonts.googleapis.com/css2?family=Roboto+Condensed:wght@300;400;700&display=swap" rel="stylesheet">
<style>
  :root{
    --orange:#ef7d00;
    --grey-bg:#e4e4e4;
    --navy:#0b1f5e;
    --navy-deep:#071640;
    --blue:#1a4fb8;
    --ink:#2b2b2b;
    --bar-grey:#9a9a9a;
    --white:#ffffff;
  }
  *{box-sizing:border-box;margin:0;padding:0}
  html,body{width:1200px;height:2367px;overflow:hidden}
  body{position:relative;background:var(--grey-bg);font-family:"Roboto Condensed",Arial,sans-serif;color:var(--ink)}
  .backdrop{position:absolute;inset:0}
  .showcase-title{position:absolute;left:83px;top:168px;color:var(--ink);font-weight:300;line-height:.9}
  .showcase-title .line-1{font-size:92px;letter-spacing:1px;color:#1d1d1d}
  .showcase-title .line-2{font-size:150px;color:var(--white);margin-top:6px}
  .showcase-title .line-3{font-size:92px;color:var(--white);text-align:right;width:446px;margin-top:-2px}

  .page{position:absolute;background:var(--white);width:496px;height:702px;box-shadow:0 4px 12px rgba(0,0,0,.25);overflow:hidden}
  .photo{position:absolute}
  .footer{position:absolute;left:0;right:0;top:678px;font-size:7.5px;text-align:center;display:flex;justify-content:center;align-items:center;gap:5px;color:#333}
  .footer .dot{width:6px;height:6px;border-radius:50%;background:var(--orange)}
  .body-text{position:absolute;font-size:8.1px;line-height:1.36;text-align:justify;color:#222}
  .body-text p+p{margin-top:8px}
  .heading{position:absolute;color:var(--orange);font-weight:700}

  /* cover */
  .cover{left:619px;top:81px}
  .brand{position:absolute;top:36px;left:0;right:0;display:flex;justify-content:center;align-items:center;gap:10px}
  .brand .mark{width:14px;height:14px;border-radius:50%;background:var(--orange)}
  .brand .name{font-size:20px;letter-spacing:4px;line-height:1;color:#666;font-weight:400}
  .cover-band{position:absolute;top:101px;left:0;width:496px;height:484px;background:radial-gradient(ellipse at 30% 30%,#2f7ee8 0%,#123a9c 35%,var(--navy) 70%,var(--navy-deep) 100%)}
  .cover-acronym{position:absolute;left:29px;top:290px;font-size:104px;font-weight:700;color:var(--white);letter-spacing:-1px}
  .cover-subtitle{position:absolute;left:29px;top:400px;font-size:27px;font-weight:700;color:var(--white);letter-spacing:.3px}
  .cover-thumb{top:523px;width:131px;height:129px;border:3px solid var(--white)}

  /* index */
  .index{left:82px;top:838px}
  .index-strip{left:0;top:0;width:157px;height:702px;background:radial-gradient(ellipse at 60% 20%,#1f5bd0 0%,#0d2a80 40%,var(--navy-deep) 100%)}
  .index .heading{left:192px;top:374px;font-size:19px}
  .toc{position:absolute;left:192px;top:433px;width:200px;list-style:none;font-size:11px}
  .toc li{display:flex;justify-content:space-between;height:28px}

  /* intro */
  .intro{left:620px;top:838px}
  .intro-hero{left:0;top:0;width:496px;height:202px;background:linear-gradient(100deg,#0a1a44 0%,#2a5bb0 45%,#5b8ad0 60%,#0d2a70 100%)}
  .intro .heading{left:0;right:0;text-align:center;top:110px;font-size:31px}
  .intro .body-text{left:29px;top:250px;width:205px}
  .intro-box{position:absolute;left:247px;top:254px;width:249px;height:368px;background:var(--navy);padding:46px 27px 0 27px}
  .intro-box .body-text{position:static;color:var(--white)}

  /* research */
  .research{left:80px;top:1580px}
  .research .heading{left:30px;top:184px;font-size:19px}
  .research .col-a{left:30px;top:212px;width:204px}
  .research .col-b{left:262px;top:192px;width:205px}
  .survey-strip{position:absolute;left:30px;top:368px;width:437px;text-align:center}
  .survey-strip .caption{font-size:6.6px;color:#555}
  .survey-strip .cells{display:flex;justify-content:center;gap:2px;margin:6px 0 3px}
  .survey-strip .cell{width:9px;height:11px;border:1px solid}
  .survey-strip .legend{display:flex;justify-content:space-around;font-size:5.6px}
  .research .col-c{left:30px;top:543px;width:204px}
  .research .col-d{left:262px;top:543px;width:205px}

  /* fears */
  .fears{left:620px;top:1582px}
  .fears .heading{left:0;right:0;text-align:center;top:32px;font-size:19px}
  .fears .lead{left:29px;top:62px;width:438px}
  .band{position:absolute;left:0;width:496px;height:31px;background:var(--navy);color:var(--white);font-size:8px;display:flex;align-items:center;justify-content:center}
  .bar-chart{position:absolute;left:0;top:168px;width:496px;list-style:none}
  .bar-chart li{display:flex;align-items:center;height:14px}
  .bar-chart .label{width:305px;text-align:right;font-size:5.4px;padding-right:17px;color:#222}
  .bar-chart .bar{height:10px;font-size:7px;color:var(--white);text-align:right;padding-right:4px;line-height:10px}
  .bar.is-orange{background:var(--orange)}
  .bar.is-grey{background:var(--bar-grey)}
  .fears-photo{left:0;top:334px;width:239px;height:138px;background:linear-gradient(135deg,#050c26 0%,#1646b0 45%,#3f86ea 60%,#0a1c55 100%)}
  .fears .side{left:262px;top:334px;width:205px}
  .line-chart{position:absolute;left:0;top:513px}
</style>
</head>
<body>

<svg class="backdrop" width="1200" height="2367" aria-hidden="true">
  <polygon points="0,0 1200,0 1200,528 0,1505" fill="var(--orange)"/>
</svg>

<h1 class="showcase-title">
  <div class="line-1">POWERPOINT</div>
  <div class="line-2">REPORT</div>
  <div class="line-3">design</div>
</h1>

<!-- Cover -->
<section class="page cover">
  <div class="brand"><span class="mark"></span><span class="name">CORVAL<br>MEADOW</span></div>
  <div class="cover-band" role="img" aria-label="Blue digital globe with glowing network lines"></div>
  <div class="cover-acronym">OST</div>
  <div class="cover-subtitle">OSSERVATORIO SCREEN TIDES</div>
  <div class="photo cover-thumb" style="left:29px;background:linear-gradient(160deg,#e9ecef,#8a8f96)" role="img" aria-label="Hand touching a virtual screen"></div>
  <div class="photo cover-thumb" style="left:183px;background:linear-gradient(160deg,#f4f5f6,#b9c2c8)" role="img" aria-label="Hands with smartphone and tablet showing charts"></div>
  <div class="photo cover-thumb" style="left:337px;background:linear-gradient(160deg,#eef0f2,#9ea3a9)" role="img" aria-label="Hands typing on a laptop with network icons"></div>
</section>

<!-- Index -->
<section class="page index">
  <div class="photo index-strip" role="img" aria-label="Blue particle wave on dark background"></div>
  <h2 class="heading">Indice</h2>
  <ol class="toc">
    <li><span>Capitolo 1</span><span>01</span></li>
    <li><span>Capitolo 1</span><span>04</span></li>
    <li><span>Capitolo 1</span><span>10</span></li>
    <li><span>Capitolo 1</span><span>15</span></li>
    <li><span>Capitolo 1</span><span>20</span></li>
    <li><span>Capitolo 1</span><span>24</span></li>
    <li><span>Capitolo 1</span><span>28</span></li>
  </ol>
  <div class="footer"><span class="dot"></span>La dimensione digitale della vita | dicembre 2020 | © Corvalmeadow 2020 | Page 2</div>
</section>

<!-- Introduction -->
<section class="page intro">
  <div class="photo intro-hero" role="img" aria-label="Businessman touching a digital world map with glowing globes"></div>
  <h2 class="heading">Introduzione</h2>
  <div class="body-text">
    <p>Il digitale ha cambiato il mondo a un livello di profondità di cui non siamo ancora pienamente consapevoli. È facile riconoscere le manifestazioni del digitale nei comportamenti delle persone e notare come ha formato nuove abitudini e ritualità quotidiane. Non è altrettanto immediato comprendere quanto il digitale abbia modificato il mondo interiore e abbia inciso sul senso dell'identità, sulle emozioni in gioco nelle relazioni, su affetti e sessualità, sul modo di concepire la società, i diritti e la libertà personale.</p>
    <p>L'obiettivo di questo lavoro di ricerca è raccontare la struttura e l'evoluzione di alcuni atteggiamenti di fondo che influenzano i comportamenti quotidiani legati alle tecnologie digitali. Le informazioni sono ricavate dalle dichiarazioni di campioni di individui chiamati a riflettere sull'ambiente connesso, cioè l'insieme di tutte le relazioni e attività che si possono svolgere grazie alla Rete e, più in generale, grazie a tutte le innovazioni introdotte dagli strumenti e dai servizi digitali.</p>
    <p>L'analisi indaga le dinamiche cognitive e psicologiche che originano i comportamenti e descrive gli orientamenti di base sottostanti alle scelte – talvolta inconsapevoli – che danno forma alla dimensione digitale della vita. Questa, infatti, può assumere una configurazione molto diversa dalla dimensione della vita di prima, intendendo con questo la vita non mediata dagli strumenti dell'ICT: persone introverse nella vita naturale possono avere una vita digitale ricca di relazioni e attività, così come persone di orientamento liberale possono assumere atteggiamenti reazionari nella dimensione digitale della vita.</p>
  </div>
  <div class="intro-box">
    <div class="body-text">
      <p>La recente esperienza del lockdown per il Covid-19 ha accelerato l'evoluzione del fenomeno e ha esasperato alcuni aspetti della dimensione digitale della vita. Per alcuni mesi il mondo è stato un inedito e prezioso laboratorio di psicologia sociale: le forme digitali delle relazioni personali e sociali hanno prevalso e sostituito quelle della vita naturale e hanno generato riflessioni non astratte ma elaborate sulla base delle esperienze vissute. Per questi motivi Corval Meadow ha prodotto le analisi dei dati e ha anticipato l'uscita di questo Rapporto, anche se il lavoro ha l'obiettivo di seguire i fenomeni per un tempo più lungo, di almeno un decennio.</p>
      <p>Le innovazioni dell'epoca moderna hanno generato benessere diffuso: dalla medicina all'elettricità, dalla diffusione della conoscenza alla produzione e distribuzione dei prodotti alimentari. La domanda che ci poniamo oggi è relativa alle tecnologie digitali: ci renderanno la vita più facile, la convivenza più pacifica, ci daranno una salute migliore?</p>
      <p>In definitiva, il digitale ci renderà più felici?</p>
    </div>
  </div>
  <div class="footer"><span class="dot"></span>La dimensione digitale della vita | dicembre 2020 | © Corvalmeadow 2020 | Page 3</div>
</section>

<!-- Research -->
<section class="page research">
  <div class="photo" style="left:0;top:0;width:322px;height:149px;background:radial-gradient(circle at 50% 50%,#3d8cf0 0%,#1450c0 45%,#0a2a80 100%)" role="img" aria-label="Shopping cart icon on a blue circuit board"></div>
  <div class="photo" style="left:329px;top:0;width:167px;height:149px;background:linear-gradient(135deg,#f2f2f2,#c9c9c9)" role="img" aria-label="Woman looking at her smartphone"></div>
  <h2 class="heading">La ricerca</h2>
  <div class="body-text col-a">
    <p>"L'ambiente connesso è tutto ciò che accade perché siamo connessi alla rete: tutti i modi che, grazie alla connessione alla rete, abbiamo per comunicare con altre persone e tessere relazioni, per fruire di contenuti di tutti i tipi (informazioni testuali, video, musica, giochi etc), per acquistare prodotti e utilizzare servizi (bancari, amministrativi, pagamenti), o utilizzare nuove tecnologie per la casa, per la mobilità, per il fitness e la salute, etc… Alcune di queste attività fanno ormai parte della nostra vita quotidiana, altre probabilmente lo diventeranno nei prossimi anni. Ecco, tutto questo compone l'ambiente connesso.</p>
  </div>
  <div class="body-text col-b">
    <p>La popolazione online riesce quindi a rappresentare quella fetta di società italiana maggiormente impattata dal fenomeno della digitalizzazione e del mondo connesso, anche se con livelli di consapevolezza, stress, paure e atteggiamenti completamente diversi che descrivono «mondi» molto diversi.</p>
    <p>L'esigenza di capire il vissuto degli italiani su questi temi è nata in Corval Meadow nel 2018 e si è concretizzata con la prima rilevazione a Gennaio 2019, momento in cui si è «fotografata» per la prima volta la situazione. Poiché il fenomeno descritto è in continua evoluzione e cambiamento, si è scelto di monitorarlo con una rilevazione semestrale ma l'emergenza Covid-19 ha reso necessario</p>
  </div>
  <div class="survey-strip">
    <div class="caption">Analisi di 27 aspetti dell'impatto del digitale nella vita quotidiana: interviste a un campione di popolazione maggiorenne</div>
    <div class="cells">
      <span class="cell" style="border-color:#666"></span><span class="cell" style="border-color:#666"></span><span class="cell" style="border-color:#666"></span><span class="cell" style="border-color:#666"></span><span class="cell" style="border-color:#666"></span><span class="cell" style="border-color:#666"></span><span class="cell" style="border-color:#666"></span><span class="cell" style="border-color:#666"></span>
      <span class="cell" style="border-color:#2e8b3a"></span><span class="cell" style="border-color:#2e8b3a"></span><span class="cell" style="border-color:#2e8b3a"></span><span class="cell" style="border-color:#2e8b3a"></span><span class="cell" style="border-color:#2e8b3a"></span><span class="cell" style="border-color:#2e8b3a"></span><span class="cell" style="border-color:#2e8b3a"></span><span class="cell" style="border-color:#2e8b3a"></span>
      <span class="cell" style="border-color:#2a6cc9"></span><span class="cell" style="border-color:#2a6cc9"></span><span class="cell" style="border-color:#2a6cc9"></span><span class="cell" style="border-color:#2a6cc9"></span><span class="cell" style="border-color:#2a6cc9"></span><span class="cell" style="border-color:#2a6cc9"></span><span class="cell" style="border-color:#2a6cc9"></span>
      <span class="cell" style="border-color:var(--orange)"></span><span class="cell" style="border-color:var(--orange)"></span><span class="cell" style="border-color:var(--orange)"></span><span class="cell" style="border-color:var(--orange)"></span><span class="cell" style="border-color:var(--orange)"></span><span class="cell" style="border-color:var(--orange)"></span><span class="cell" style="border-color:var(--orange)"></span>
      <span class="cell" style="border-color:#d8202a"></span><span class="cell" style="border-color:#d8202a"></span><span class="cell" style="border-color:#d8202a"></span><span class="cell" style="border-color:#d8202a"></span><span class="cell" style="border-color:#d8202a"></span><span class="cell" style="border-color:#d8202a"></span><span class="cell" style="border-color:#d8202a"></span>
    </div>
    <div class="legend">
      <span style="color:#666">8 domande sulle paure</span>
      <span style="color:#2e8b3a">8 domande sulle speranze</span>
      <span style="color:#2a6cc9">7 di atteggiamento</span>
      <span style="color:var(--orange)">7 su Dati &amp; Privacy</span>
      <span style="color:#d8202a">7 sulla società digitale</span>
    </div>
  </div>
  <div class="photo" style="left:0;top:419px;width:496px;height:112px;background:linear-gradient(90deg,#06080f 0%,#1b2230 50%,#05070c 100%)" role="img" aria-label="Hand touching a dark interface with data dials"></div>
  <div class="body-text col-c">
    <p>La ricerca si basa sull'analisi di 27 aspetti dell'impatto delle nuove tecnologie nella vita quotidiana e 19 ulteriori informazioni sui comportamenti abituali e i giudizi su alcuni temi rese da un campione di rispondenti rappresentativo degli oltre 40 milioni di italiani online. Gli italiani online sono ormai la grande maggioranza della popolazione italiana: la quasi totalità tra i più giovani ma anche tra la popolazione anziana l'utilizzo di Internet diventa sempre più diffuso di anno in anno.</p>
  </div>
  <div class="body-text col-d">
    <p>intensificare le rilevazioni, che nel 2020 sono state tre: una pre-emergenza, una durante il primo lockdown primaverile e una durante il secondo autunnale. Nel documento sono mostrati i risultati relativi a cinque wave di ricerca che ci permettono di descrivere il mondo Pre e Post pandemia. Alcuni trend rilevati sono di lungo periodo e ci accompagneranno anche col ritorno alla «normalità», altri sono invece transitori e destinati ad affievolirsi con l'allontanarsi dell'emergenza.</p>
  </div>
  <div class="footer"><span class="dot"></span>La dimensione digitale della vita | dicembre 2020 | © Corvalmeadow 2020 | Page 4</div>
</section>

<!-- Fears -->
<section class="page fears">
  <h2 class="heading">Le paure</h2>
  <div class="body-text lead">
    <p>Il digitale può fare paura per le conseguenze che produce nelle capacità cognitive, nelle relazioni personali e sociali, fino a quelle internazionali. Molti non conoscono cosa c'è dietro e da dove vengono certe magie della tecnologia, alle quali ci siamo abituati e che non ci meravigliano più ma rimangono in gran parte incomprensibili. Inoltre, certi racconti sulle sorveglianza digitale e sui nuovi poteri che emergono dai dati ispirano un senso di sospetto condiviso da un'ampia maggioranza di individui.</p>
  </div>
  <div class="band" style="top:129px">Le paure e i sospetti</div>
  <ul class="bar-chart">
    <li><span class="label">Nell'ambiente connesso è più facile manipolare le persone</span><span class="bar is-orange" style="width:97px">80%</span></li>
    <li><span class="label">I ragazzi hanno notevoli problemi di socializzazione a causa del digitale</span><span class="bar is-grey" style="width:93px">77%</span></li>
    <li><span class="label">Alcuni servizi sanno tutto di noi: chi vediamo, cosa facciamo, cosa scriviamo e diciamo, anche…</span><span class="bar is-orange" style="width:91px">75%</span></li>
    <li><span class="label">I dispositivi che utilizzo mandano continuamente dati su di me a organizzazioni di cui ignoro…</span><span class="bar is-grey" style="width:86px">71%</span></li>
    <li><span class="label">Le notizie online ci fanno perdere la capacità di distinguere il vero dal falso</span><span class="bar is-orange" style="width:85px">70%</span></li>
    <li><span class="label">Il digitale diminuisce la capacità di apprendimento a tutte le età</span><span class="bar is-grey" style="width:51px">42%</span></li>
    <li><span class="label">Le democrazie sono a rischio a causa della diffusione dell'odio online</span><span class="bar is-orange" style="width:42px">35%</span></li>
    <li><span class="label">Prossimamente ci sarà una guerra cibernetica fra Stati</span><span class="bar is-grey" style="width:40px">33%</span></li>
  </ul>
  <div class="band" style="top:292px">Incidenza sul totale campione dei Top2Box di accordo, in una scala a 5 passi (1.017 casi a novembre 2020)</div>
  <div class="photo fears-photo" role="img" aria-label="Abstract blue light streaks in perspective"></div>
  <div class="body-text side">
    <p>Il sospetto che il flusso di informazioni generato dalle tecnologie sia utilizzato con finalità di controllo o manipolazione è molto diffuso e riguarda otto individui sui dieci. Il 77% si dichiara d'accordo con l'affermazione secondo la quale il digitale crea problemi di socialità nei ragazzi e il dato aumenta tra le persone oltre i 54 anni di età. Così come tra i meno giovani trova conferma l'idea, già piuttosto diffusa, che il digitale diminuisca le capacità di apprendimento. Le paure sulle conseguenze politiche e sociali del digitale sono più contenute ma riguardano pur sempre un terzo della popolazione.</p>
  </div>
  <div class="band" style="top:483px">Il trend dell'indice di paura</div>
  <svg class="line-chart" width="496" height="119" viewBox="0 0 496 119" role="img" aria-label="Indice di paura: feb 19 58%, ott 19 59%, feb 20 62%, mag 20 60%, nov 20 60%">
    <path d="M80,73 C120,70 140,66 162,62 C200,48 220,28 243,28 C270,28 300,52 325,52 C360,52 380,46 407,43" fill="none" stroke="var(--orange)" stroke-width="1.2"/>
    <g fill="var(--orange)">
      <circle cx="80" cy="73" r="3.2"/><circle cx="162" cy="62" r="3.2"/><circle cx="243" cy="28" r="3.2"/><circle cx="325" cy="52" r="3.2"/><circle cx="407" cy="43" r="3.2"/>
    </g>
    <g font-size="8" fill="#222" text-anchor="middle" font-family="Roboto Condensed, sans-serif">
      <text x="80" y="89">58%</text><text x="162" y="78">59%</text><text x="243" y="20">62%</text><text x="325" y="68">60%</text><text x="407" y="59">60%</text>
      <text x="78" y="114">feb 19</text><text x="160" y="114">ott 19</text><text x="241" y="114">feb 20</text><text x="323" y="114">mag 20</text><text x="405" y="114">nov 20</text>
    </g>
  </svg>
  <div class="band" style="top:632px">L'indice di paura è ottenuto come media semplice dei Top2Box delle otto voci analizzate</div>
  <div class="footer" style="top:682px"><span class="dot"></span>La dimensione digitale della vita | dicembre 2020 | © Corvalmeadow 2020 | Page 5</div>
</section>

</body>
</html>
```